Exciting Personal Development Book Cover: FIND ZEN NOW!

Design a Book Cover for my personal development book.
Title: Find Zen Now!
Author: Marcus Telly
Tagline: A real-life solution to get unstuck and break free

My picture must make up the front cover as I need to build my brand and people should recognise me on book shelves. Bold and catchy. How you do it is up to you. There must be space for a short testimonial from a famous person who is currently reading my book. I uploaded a sample of what I made in Photoshop but I don't have design skills.

I've added a PDF of my book so you can read the chapter index and introduction to get a sense of the content.

Target Market(s)

Personal Development Self-Help Market

Industry/Entity Type

Personal Development

Font styles to use
Serif
Sans Serif

Requirements
Must have
• My picture as hero image on cover.
Nice to have
• Must have Title, Tagline and my author name. If possible ZEN stands for 'Zeal, Energy & Nerve' If there is a way to fit this somewhere great. If it's too much then it can go somewhere on the back.

```html
<!DOCTYPE html>
<html lang="en">
<head>
<meta charset="utf-8">
<title>Find Zen Now! — Marcus Telly</title>
<link rel="stylesheet" href="https://fonts.googleapis.com/css2?family=Anton&family=Roboto+Condensed:ital,wght@0,400;0,700;1,700;1,800&display=swap">
<style>
  :root {
    --cover-black: #000000;
    --brand-blue: #00aeef;
    --border-blue: #29a9e0;
    --title-white: #ffffff;
    --shirt-light: #d6d4d6;
    --shirt-mid: #8e8c8e;
    --shirt-shadow: #2a2a2a;
    --skin-tone: #b08870;
    --skin-shadow: #5a3e30;
  }
  html, body {
    margin: 0;
    padding: 0;
    width: 811px;
    height: 1200px;
    overflow: hidden;
    background: var(--cover-black);
  }
  .book-cover {
    display: block;
    width: 811px;
    height: 1200px;
  }
  .title-word {
    font-family: "Anton", "Impact", sans-serif;
  }
  .title-word--white { fill: var(--title-white); }
  .title-word--blue { fill: var(--brand-blue); }
  .acronym-line {
    font-family: "Roboto Condensed", "Arial Narrow", sans-serif;
    font-weight: 800;
    font-style: italic;
    fill: var(--title-white);
  }
  .tagline {
    font-family: "Roboto Condensed", "Arial Narrow", sans-serif;
    font-weight: 400;
    fill: var(--brand-blue);
  }
  .author-name {
    font-family: "Roboto Condensed", "Arial Narrow", sans-serif;
    font-weight: 700;
    fill: var(--brand-blue);
  }
  .cover-frame {
    fill: none;
    stroke: var(--border-blue);
    stroke-width: 1.5;
    stroke-dasharray: 3 3;
  }
</style>
</head>
<body>
<svg class="book-cover" viewBox="0 0 811 1200" xmlns="http://www.w3.org/2000/svg">
  <defs>
    <radialGradient id="shirt-tone" cx="405" cy="640" r="420" gradientUnits="userSpaceOnUse" gradientTransform="translate(405 640) scale(1 0.85) translate(-405 -640)">
      <stop offset="0%" stop-color="var(--shirt-light)"/>
      <stop offset="55%" stop-color="var(--shirt-mid)"/>
      <stop offset="85%" stop-color="var(--shirt-shadow)"/>
      <stop offset="100%" stop-color="var(--cover-black)" stop-opacity="0"/>
    </radialGradient>
    <radialGradient id="head-tone" cx="405" cy="250" r="170" gradientUnits="userSpaceOnUse" gradientTransform="translate(405 250) scale(0.85 1.25) translate(-405 -250)">
      <stop offset="0%" stop-color="var(--skin-tone)"/>
      <stop offset="65%" stop-color="var(--skin-shadow)"/>
      <stop offset="100%" stop-color="var(--cover-black)" stop-opacity="0"/>
    </radialGradient>
    <linearGradient id="lower-fade" x1="0" y1="0" x2="0" y2="1">
      <stop offset="0%" stop-color="var(--cover-black)" stop-opacity="0"/>
      <stop offset="100%" stop-color="var(--cover-black)" stop-opacity="0.9"/>
    </linearGradient>
  </defs>

  <rect class="cover-background" x="0" y="0" width="811" height="1200" fill="var(--cover-black)"/>

  <g class="author-photo" role="img" aria-label="Portrait photograph of the author smiling in a white open-collar shirt with sleeves rolled up and tattooed forearms, against a black background">
    <rect x="20" y="20" width="771" height="1160" fill="url(#shirt-tone)"/>
    <rect x="20" y="20" width="771" height="520" fill="url(#head-tone)"/>
    <rect x="20" y="900" width="771" height="280" fill="url(#lower-fade)"/>
  </g>

  <rect class="cover-frame" x="16" y="16" width="779" height="1168"/>

  <g class="cover-title">
    <text class="title-word title-word--white" x="61" y="809" font-size="237" textLength="211" lengthAdjust="spacingAndGlyphs">FIND</text>
    <text class="title-word title-word--blue" x="272" y="911" font-size="362" textLength="329" lengthAdjust="spacingAndGlyphs">ZEN</text>
    <text class="title-word title-word--white" x="606" y="911" font-size="236" textLength="150" lengthAdjust="spacingAndGlyphs">NOW!</text>
  </g>

  <text class="acronym-line" x="405" y="968" font-size="46" text-anchor="middle" textLength="525" lengthAdjust="spacingAndGlyphs">Zeal, Energy &amp; Nerve</text>

  <text class="tagline" x="405" y="1009" font-size="31" text-anchor="middle" textLength="631" lengthAdjust="spacing">A real-life solution to get unstuck and break free</text>

  <text class="author-name" x="405" y="1125" font-size="44" text-anchor="middle" textLength="323" lengthAdjust="spacingAndGlyphs">MARCUS TELLY</text>
</svg>
</body>
</html>
```